Postcard Design Project

Underground fencing for dogs (Invisible dog fencing) a postcard for my customers
"Keeping in touch with them" offering them $25.00 service call/ $75.00 install I My Logo on my truck/paper work is the Girl & Dog touching noises.

Fencing

```html
<!DOCTYPE html>
<html lang="en">
<head>
<meta charset="utf-8">
<title>Maplewood Pet Containment – Special Savings Postcard</title>
<link rel="stylesheet" href="https://fonts.googleapis.com/css2?family=Alfa+Slab+One&family=Oswald:wght@500;700&family=Roboto+Condensed:wght@400;700&family=Libre+Baskerville:wght@700&display=swap">
<style>
  :root{
    --canvas:#d9dadb;
    --yellow:#e9d72c;
    --teal:#1f9a85;
    --teal-dark:#147866;
    --title-green:#1fa37a;
    --red:#e3201b;
    --orange:#f39a1e;
    --ink:#2a2326;
    --arc:#4b4b4b;
    --white:#ffffff;
    --text-dark:#2b2b2b;
  }
  *{margin:0;padding:0;box-sizing:border-box}
  html,body{width:1200px;height:1200px;overflow:hidden}
  body{background:var(--canvas);position:relative;font-family:"Roboto Condensed",Arial,sans-serif}
  .card{position:absolute;overflow:hidden;background:var(--white);transform-origin:0 0;transform:scale(.8);box-shadow:0 10px 30px rgba(0,0,0,.25)}
  .card--back{width:890px;height:585px;left:64px;top:134px}
  .card--front{width:585px;height:890px;left:611px;top:413px}
  .card svg.art{position:absolute;left:0;top:0}
  .t{position:absolute;line-height:1;white-space:nowrap}
  .title{font-family:"Alfa Slab One",Georgia,serif;color:var(--title-green);text-shadow:2px 2px 0 var(--white),-1px -1px 0 var(--white);letter-spacing:1px}
  .offer{font-family:"Oswald",Impact,sans-serif;font-weight:700;color:var(--red);text-align:center;transform:translateX(-50%)}
  .offer small{font-size:.7em}
  .offer-note{font-family:"Roboto Condensed",Arial,sans-serif;font-size:13px;color:var(--text-dark);text-align:center;transform:translateX(-50%);line-height:17px}
  .brand{font-family:"Roboto Condensed",Arial,sans-serif;font-weight:700;color:var(--white);letter-spacing:1px}
  .brand-sub{font-family:"Roboto Condensed",Arial,sans-serif;font-weight:400;color:var(--white);letter-spacing:2.5px}
  .batteries{font-family:"Oswald",Impact,sans-serif;font-weight:700;color:var(--white);text-shadow:1px 2px 3px rgba(0,0,0,.5)}
  .batteries small{font-family:"Roboto Condensed",Arial,sans-serif;font-weight:400;font-size:24px}
  .batteries-note{font-family:"Roboto Condensed",Arial,sans-serif;color:var(--white);font-size:22px;text-shadow:1px 1px 2px rgba(0,0,0,.5)}
  .email-pill{font-family:"Roboto Condensed",Arial,sans-serif;color:var(--ink);font-size:25px}
  .starburst-text{font-family:"Alfa Slab One",Georgia,serif;color:var(--white);font-size:29px;line-height:30px;text-align:center;transform:rotate(-16deg);text-shadow:1px 1px 2px rgba(0,0,0,.35)}
  .priority{font-family:"Oswald",Impact,sans-serif;font-weight:700;color:var(--white);font-size:26px;text-align:right;line-height:33px;text-shadow:1px 1px 3px rgba(0,0,0,.8)}
  .approved{font-family:"Roboto Condensed",Arial,sans-serif;font-weight:700;color:var(--text-dark);font-size:29px}
  .tagline{font-family:"Libre Baskerville",Georgia,serif;font-weight:700;color:var(--white);font-size:20px;font-variant:small-caps;text-align:center;width:585px;left:0}
  .tagline span{font-size:15px}
  .cta{font-family:"Oswald",Impact,sans-serif;font-weight:700;font-size:27px;text-align:center;width:585px;left:0;color:var(--white)}
  .cta em{font-style:normal;color:var(--orange)}
  .footer-email{font-family:"Roboto Condensed",Arial,sans-serif;color:var(--orange);font-size:21px;text-align:center;width:585px;left:0}
</style>
</head>
<body>

<section class="card card--back" aria-label="Postcard address side">
  <svg class="art" width="890" height="585" viewBox="0 0 890 585">
    <defs>
      <linearGradient id="backScene" x1="0" y1="0" x2="0" y2="1">
        <stop offset="0" stop-color="#3e7d55"/>
        <stop offset=".6" stop-color="#4f8f45"/>
        <stop offset="1" stop-color="#3f8a3a"/>
      </linearGradient>
      <radialGradient id="badge" cx=".45" cy=".4" r=".65">
        <stop offset="0" stop-color="#ffffff"/>
        <stop offset=".55" stop-color="#e2e2e2"/>
        <stop offset="1" stop-color="#8d8d8d"/>
      </radialGradient>
      <linearGradient id="photoA" x1="0" y1="0" x2="1" y2="1">
        <stop offset="0" stop-color="#6f8f6a"/><stop offset="1" stop-color="#3a4a5a"/>
      </linearGradient>
      <linearGradient id="photoB" x1="0" y1="0" x2="0" y2="1">
        <stop offset="0" stop-color="#7ea35e"/><stop offset="1" stop-color="#5d6266"/>
      </linearGradient>
      <radialGradient id="logoFill" cx=".5" cy=".5" r=".6">
        <stop offset="0" stop-color="#e7b98a"/><stop offset="1" stop-color="#6b5a4a"/>
      </radialGradient>
    </defs>
    <path role="img" aria-label="Photo of a technician with a dog on a garden lawn" d="M0 0 H620 C530 150 520 420 610 585 H0 Z" fill="url(#backScene)"/>
    <path d="M0 0 H620 C600 60 560 100 500 112 C400 130 250 112 0 135 Z" fill="var(--teal)"/>
    <path d="M0 0 H625 C585 55 520 92 420 100 C300 108 150 70 0 48 Z" fill="var(--yellow)"/>
    <path d="M622 0 C532 150 522 420 612 585" fill="none" stroke="var(--arc)" stroke-width="22"/>
    <g transform="rotate(-8 125 203)">
      <rect x="20" y="118" width="210" height="170" fill="var(--white)"/>
      <rect role="img" aria-label="Photo of the owner with his dog" x="28" y="126" width="194" height="154" fill="url(#photoA)"/>
    </g>
    <g transform="rotate(-6 317 215)">
      <rect x="212" y="130" width="210" height="170" fill="var(--white)"/>
      <rect role="img" aria-label="Photo of a trainer working with a dog on a driveway" x="220" y="138" width="194" height="154" fill="url(#photoB)"/>
    </g>
    <circle cx="580" cy="90" r="78" fill="var(--white)"/>
    <circle cx="580" cy="90" r="71" fill="url(#badge)"/>
    <circle cx="490" cy="257" r="88" fill="var(--white)"/>
    <circle cx="490" cy="257" r="80" fill="url(#badge)"/>
    <circle cx="80" cy="370" r="50" fill="var(--white)"/>
    <circle cx="80" cy="370" r="43" fill="url(#logoFill)"/>
    <rect x="735" y="32" width="105" height="105" fill="#e6e6e6"/>
    <g stroke="#555" stroke-width="1.5">
      <line x1="618" y1="292" x2="850" y2="292"/>
      <line x1="618" y1="330" x2="850" y2="330"/>
      <line x1="618" y1="372" x2="850" y2="372"/>
      <line x1="618" y1="414" x2="850" y2="414"/>
    </g>
    <path d="M0 512 H377 Q405 512 405 540 Q405 569 377 569 H0 Z" fill="var(--yellow)"/>
  </svg>

  <div class="t title" style="left:75px;top:32px;font-size:40px">SPECIAL SAVINGS</div>

  <div class="t offer" style="left:580px;top:58px;font-size:33px">25.00 <small>OFF</small></div>
  <div class="t offer-note" style="left:580px;top:92px">SERVICE<br>CALLS REPAIRS<br>MAINTENANCE</div>

  <div class="t offer" style="left:490px;top:205px;font-size:35px">75$ <small>OFF</small></div>
  <div class="t offer-note" style="left:490px;top:246px">COMPLETE<br>PET CONTAINMENT<br>SYSTEM INSTALLATION</div>

  <div class="t brand" style="left:143px;top:342px;font-size:38px">MAPLEWOOD</div>
  <div class="t brand-sub" style="left:143px;top:382px;font-size:18px">PET CONTAINMENT LLC</div>

  <div class="t batteries" style="left:40px;top:426px;font-size:38px">FREE BATTERIES <small>FOR</small></div>
  <div class="t batteries-note" style="left:44px;top:471px">ONE YEAR IF THEY E-MAIL ME BACK</div>

  <div class="t email-pill" style="left:48px;top:526px">maplewoodpetfence@mail.com</div>
</section>

<section class="card card--front" aria-label="Postcard picture side">
  <svg class="art" width="585" height="890" viewBox="0 0 585 890">
    <defs>
      <linearGradient id="frontField" x1="0" y1="0" x2="0" y2="1">
        <stop offset="0" stop-color="#e9d72c"/>
        <stop offset=".45" stop-color="#b9cf3e"/>
        <stop offset=".7" stop-color="#7fb84a"/>
      </linearGradient>
      <linearGradient id="frontScene" x1="0" y1="0" x2="1" y2="1">
        <stop offset="0" stop-color="#4d7a3f"/>
        <stop offset=".5" stop-color="#5b5046"/>
        <stop offset="1" stop-color="#3f3a36"/>
      </linearGradient>
      <linearGradient id="burst" x1="0" y1="0" x2="0" y2="1">
        <stop offset="0" stop-color="#d9e02a"/>
        <stop offset=".5" stop-color="#5fb34c"/>
        <stop offset="1" stop-color="#138a70"/>
      </linearGradient>
      <radialGradient id="badgeF" cx=".45" cy=".4" r=".65">
        <stop offset="0" stop-color="#ffffff"/>
        <stop offset=".55" stop-color="#e2e2e2"/>
        <stop offset="1" stop-color="#8d8d8d"/>
      </radialGradient>
      <radialGradient id="logoFillF" cx=".5" cy=".5" r=".6">
        <stop offset="0" stop-color="#e7b98a"/><stop offset="1" stop-color="#6b5a4a"/>
      </radialGradient>
    </defs>
    <rect width="585" height="890" fill="url(#frontField)"/>
    <path role="img" aria-label="Photo of a pointer dog on a lawn in front of the company van" d="M0 0 H511 C470 220 330 460 0 600 Z" fill="url(#frontScene)"/>
    <path d="M511 0 C470 220 330 460 0 600" fill="none" stroke="var(--ink)" stroke-width="14"/>
    <path d="M0 590 C150 640 400 630 585 545 V890 H0 Z" fill="var(--teal)"/>
    <rect y="749" width="585" height="103" fill="var(--ink)"/>
    <polygon fill="url(#burst)" points="104,11 115,40 135,16 137,47 163,29 155,59 186,51 168,77 199,79 172,96 199,113 168,115 186,141 155,133 163,163 137,145 135,176 115,152 104,181 93,152 73,176 71,145 45,163 53,133 22,141 40,115 9,113 36,96 9,79 40,77 22,51 53,59 45,29 71,47 73,16 93,40"/>
    <circle cx="468" cy="184" r="80" fill="var(--white)"/>
    <circle cx="468" cy="184" r="72" fill="url(#badgeF)"/>
    <circle cx="394" cy="371" r="92" fill="var(--white)"/>
    <circle cx="394" cy="371" r="83" fill="url(#badgeF)"/>
    <circle cx="101" cy="656" r="82" fill="var(--white)"/>
    <circle cx="101" cy="656" r="74" fill="url(#logoFillF)"/>
  </svg>

  <div class="t starburst-text" style="left:34px;top:66px">SPECIAL<br>SAVINGS</div>

  <div class="t offer" style="left:468px;top:142px;font-size:34px">25.00 <small>OFF</small></div>
  <div class="t offer-note" style="left:468px;top:178px">SERVICE<br>CALLS REPAIRS<br>MAINTENANCE</div>

  <div class="t offer" style="left:394px;top:320px;font-size:38px">75$ <small>OFF</small></div>
  <div class="t offer-note" style="left:394px;top:359px">COMPLETE<br>PET CONTAINMENT<br>SYSTEM INSTALLATION</div>

  <div class="t priority" style="left:20px;top:406px;width:136px">YOUR PET'S<br>SAFETY<br>IS OUR<br>PRIORITY!</div>

  <div class="t approved" style="right:39px;top:484px">Veterinarian Approved</div>
  <div class="t approved" style="right:84px;top:524px">Underground Fencing &amp;</div>
  <div class="t approved" style="left:183px;top:562px">Training for Your Dog</div>

  <div class="t brand" style="left:203px;top:650px;font-size:50px">MAPLEWOOD</div>
  <div class="t brand-sub" style="left:203px;top:704px;font-size:24px">PET CONTAINMENT LLC</div>

  <div class="t tagline" style="top:766px">Most Experienced <span>in Fairfield County since 1995</span></div>
  <div class="t cta" style="top:793px"><em>FREE ESTIMATES!</em> CALL US NOW <em>(203) 555-0147</em></div>
  <div class="t footer-email" style="top:826px">maplewoodpetfence@mail.com</div>
</section>

</body>
</html>
```